School website design - Technology and the arts

We will need a new or updated design that incorporates the following features:
-Reactive design that changes with the needs of the device.
-Static Background - only content scrolls
-Static Menu - similar to the Wordpress Quiet harbor theme
-Alert box for important notices (closings/emergency use only) that doesn’t display unless active
-Margins must be wider than “standard wordpress theme” (fits the entire display at any resolution, doesn’t just center a columned design)
-Features an image scroll on the front page to show our current works/progress. (only if the screen is big enough). Should have swipe capability
-We must have a place on the front page to display the current school news as well as a location to display current events with a poster (see current webdesign for example)
-Uses the school colors (green and gold/yellow) in a way that is pleasing to the eye.
-Unique design to our school that is very clean and modern.
-Events need to be able to pop-out when you mouseover in a desktop environment. Example: http://plumvaultly.net/category/wordpress/creative (mouse over a theme and it shows additional information about it without a refresh)
-Custom Admin panel to easily updated the news and events section.
-Notes: We are currently using some free icons that we found to make the current site look not so boring since we do not have a lot of content on each page. We would like to step away from that and are open to suggestions. Possibly something like http://dovrami.com/demo/?theme=brook under the services section but smaller.
-Notes 2: We have plenty of pictures of our building and activities that can be used as a background, etc.
-We are open to new ideas and suggestions.

Our current website is https://www.mlvt.us to get an idea on how we manage our current site.

```html
<!DOCTYPE html>
<html lang="en">
<head>
<meta charset="utf-8">
<title>Marlowe Valley Regional Governor's School</title>
<link href="https://fonts.googleapis.com/css2?family=Arimo:wght@400;700&display=swap" rel="stylesheet">
<style>
:root{
  --backdrop:#1d5b5a;
  --green:#1d6b12;
  --green-dark:#145a0c;
  --gold:#f4c20d;
  --orange:#f7931e;
  --orange-light:#fbb03b;
  --ink:#444;
  --muted:#666;
  --line:#bbb;
  --footer:#e6e6e6;
  --footer-bar:#5a5a5a;
  --white:#fff;
}
*{margin:0;padding:0;box-sizing:border-box}
html,body{width:760px;height:1200px;overflow:hidden}
body{background:var(--backdrop);font-family:"Arimo",Arial,sans-serif;color:var(--ink);position:relative}
.page{position:absolute;left:116px;top:0;width:529px;height:1152px;background:var(--white);overflow:hidden}
.abs{position:absolute}
/* header */
.brand-mark{left:8px;top:17px;width:60px;height:60px;border-radius:50%;background:var(--gold);border:2px solid var(--green)}
.brand-name{left:87px;top:32px;font-size:14.5px;line-height:15px;color:var(--green);text-transform:uppercase}
.brand-sub{left:87px;top:70px;font-size:5.6px;color:var(--muted)}
.top-links{right:8px;top:32px;font-size:5.6px;color:var(--muted);display:flex;gap:12px}
.menu-icon{left:474px;top:64px}
.search-icon{left:508px;top:63px}
/* hero */
.hero{left:0;top:94px;width:529px;height:232px;background:linear-gradient(110deg,var(--orange) 0%,var(--orange-light) 60%,var(--orange) 100%);overflow:hidden}
.hero-title{left:58px;top:64px;font-size:24px;line-height:27px;font-weight:700;color:var(--white);text-transform:uppercase;letter-spacing:-.5px;white-space:nowrap}
.hero-photo{left:300px;top:42px;width:170px;height:190px;border-radius:80px 80px 0 0;background:linear-gradient(180deg,#f6d9c2,#ede7de 55%,#e35a4a)}
.hero-dots{left:137px;top:206px;display:flex;gap:4px}
.hero-dots span{width:4px;height:4px;border-radius:50%;background:var(--white)}
.hero-dots span:first-child{background:var(--gold)}
/* section headings */
.rule-head{left:14px;width:501px;display:flex;align-items:center;gap:12px;font-size:14px;font-weight:400;color:#555}
.rule-head::before,.rule-head::after{content:"";flex:1;height:1px;background:var(--line)}
.welcome-photo{left:93px;top:382px;width:343px;height:109px;background:linear-gradient(135deg,#3a2a24,#7a5a4a 40%,#2a2420 75%,#5a4038)}
.mission-title{left:93px;top:502px;font-size:7.5px;font-weight:400;color:var(--green)}
.mission-text{left:93px;top:516px;width:343px;font-size:5.6px;line-height:12px;color:var(--muted)}
.btn{left:239px;top:559px;width:51px;height:14px;border-radius:2px;background:var(--green);color:var(--white);font-size:5.6px;text-align:center;line-height:14px}
/* services */
.service{width:160px;text-align:center;top:632px}
.service-ring{width:84px;height:84px;border-radius:50%;border:1px solid #888;margin:0 auto;display:flex;align-items:center;justify-content:center}
.service-ring.active{background:var(--gold);border:3px solid var(--green-dark)}
.service-name{margin-top:12px;font-size:7.5px;line-height:10px;color:var(--green)}
.service-desc{margin-top:10px;font-size:5.6px;line-height:10px;color:var(--muted)}
/* columns */
.col-head{font-size:10.5px;font-weight:400;color:#555;display:flex;align-items:center;gap:8px;white-space:nowrap}
.col-head::after{content:"";flex:1;height:1px;background:#999}
.news-item{margin-top:10px}
.news-date{font-size:7.5px;color:var(--green)}
.news-text{font-size:5.6px;line-height:11px;color:var(--muted);margin-top:2px}
.event{position:absolute;left:0;width:157px;height:24px}
.event-thumb{position:absolute;left:0;top:2px;width:19px;height:17px;background:linear-gradient(180deg,#8aa,#6a7a4a)}
.event-title{position:absolute;left:27px;top:0;font-size:7.5px;color:var(--green);white-space:nowrap}
.event-place{position:absolute;left:27px;top:12px;font-size:5.6px;color:var(--muted)}
.event-btn{position:absolute;left:105px;top:1px;width:43px;height:11px;border-radius:2px;background:var(--green);color:var(--white);font-size:4.8px;line-height:11px;text-align:center}
.pager{font-size:5.6px;color:var(--ink);display:flex;align-items:center;gap:2px}
.study-photo{left:358px;top:838px;width:157px;height:58px;background:linear-gradient(120deg,#7b8fa4,#e8d2b8 45%,#7a5aa0 80%,#c0c8d4)}
.study-list{font-size:5.8px;line-height:10px;color:var(--muted)}
.study-list h4{font-size:7.5px;font-weight:400;color:var(--green);margin-bottom:3px}
.study-list li{list-style:none}
.study-list li::before{content:"› ";color:#333}
/* footer */
.footer{left:0;top:1010px;width:529px;height:123px;background:var(--footer)}
.footer-col h3{font-size:8.5px;font-weight:400;color:#555;margin-bottom:10px}
.footer-col ul{margin-left:7px;font-size:5.8px;line-height:10px;color:var(--muted);list-style:none}
.footer-col ul.social{margin-left:0}
.social li{display:flex;align-items:center;gap:5px;line-height:13px}
.dot{width:6px;height:6px;border-radius:50%}
.copyright{left:0;top:1133px;width:529px;height:19px;background:var(--footer-bar);color:var(--white);font-size:5.6px;text-align:center;line-height:19px}
</style>
</head>
<body>
<main class="page">
  <!-- header -->
  <div class="abs brand-mark"></div>
  <div class="abs brand-name">Marlowe Valley Regional<br>Governor's School</div>
  <div class="abs brand-sub">For The Arts &amp; Technology &nbsp;&nbsp; | &nbsp;&nbsp; 418 W. Linden St, 04117 555 610 0148</div>
  <nav class="abs top-links"><span>MVGS Email</span><span>Calendars</span><span>Contact us</span></nav>
  <svg class="abs menu-icon" width="19" height="12" viewBox="0 0 19 12"><g stroke="#333" stroke-width="1.3"><line x1="0" y1="1" x2="19" y2="1"/><line x1="0" y1="6" x2="19" y2="6"/><line x1="0" y1="11" x2="19" y2="11"/></g></svg>
  <svg class="abs search-icon" width="12" height="12" viewBox="0 0 12 12"><circle cx="5" cy="5" r="3.8" fill="none" stroke="#333" stroke-width="1"/><line x1="7.8" y1="7.8" x2="11.5" y2="11.5" stroke="#333" stroke-width="1.2"/></svg>

  <!-- hero -->
  <section class="abs hero">
    <div class="abs hero-photo" role="img" aria-label="Smiling student holding a stack of colourful books"></div>
    <h1 class="abs hero-title">Marlowe Valley<br>Regional<br>Governor's<br>School</h1>
    <svg class="abs" style="left:10px;top:98px" width="14" height="28" viewBox="0 0 14 28"><polyline points="13,1 1,14 13,27" fill="none" stroke="#fff" stroke-width="1.4"/></svg>
    <svg class="abs" style="left:505px;top:98px" width="14" height="28" viewBox="0 0 14 28"><polyline points="1,1 13,14 1,27" fill="none" stroke="#fff" stroke-width="1.4"/></svg>
    <div class="abs hero-dots"><span></span><span></span><span></span><span></span></div>
  </section>

  <!-- welcome -->
  <h2 class="abs rule-head" style="top:349px">Welcome to our School.</h2>
  <div class="abs welcome-photo" role="img" aria-label="Crowd of cheering students at a school event"></div>
  <h3 class="abs mission-title">Our Mission</h3>
  <p class="abs mission-text">The Marlowe Valley Regional Governor's School for the Arts and Technology provides gifted and talented students a differentiated and rigorous education, cultivates a supportive environment that inspires unique artistic and technological visions, promotes cultural tolerance, nurtures community partnerships, and produces active, engaged citizens.</p>
  <div class="abs btn">Learn More</div>

  <!-- services -->
  <h2 class="abs rule-head" style="top:595px">Services</h2>
  <div class="abs service" style="left:21px">
    <div class="service-ring"><svg width="44" height="32" viewBox="0 0 44 32"><polygon points="22,2 44,11 22,20 0,11" fill="#444"/><path d="M9 15v9c6 6 20 6 26 0v-9l-13 6z" fill="#444"/><line x1="40" y1="12" x2="40" y2="24" stroke="#444" stroke-width="1.5"/></svg></div>
    <div class="service-name">School Counseling<br>Department</div>
    <div class="service-desc">Changing your Schedule, Career Planning, Testing</div>
  </div>
  <div class="abs service" style="left:184px">
    <div class="service-ring active"><svg width="48" height="38" viewBox="0 0 48 38"><g fill="none" stroke="#222" stroke-width="2.2"><circle cx="22" cy="12" r="6"/><circle cx="9" cy="24" r="4"/><rect x="22" y="20" width="20" height="13"/><line x1="18" y1="35" x2="46" y2="35"/></g><g stroke="#222" stroke-width="3"><line x1="22" y1="2" x2="22" y2="5"/><line x1="32" y1="12" x2="29" y2="12"/><line x1="12" y1="12" x2="15" y2="12"/></g></svg></div>
    <div class="service-name">Information<br>Technology</div>
    <div class="service-desc">Help and support for technology services</div>
  </div>
  <div class="abs service" style="left:346px">
    <div class="service-ring"><svg width="42" height="32" viewBox="0 0 42 32"><path d="M21 6C15 2 7 2 2 4v26c5-2 13-2 19 2 6-4 14-4 19-2V4c-5-2-13-2-19 2zM21 6v26" fill="none" stroke="#444" stroke-width="3"/></svg></div>
    <div class="service-name">Library and<br>Media Center</div>
    <div class="service-desc">Checking out a book, device, or just come<br>to visit in a nice quiet environment.</div>
  </div>

  <!-- news -->
  <section class="abs" style="left:13px;top:810px;width:157px">
    <h2 class="col-head">Latest News</h2>
    <div class="news-item"><div class="news-date">Mon, April 7:</div><div class="news-text">Varsity Boys' Home Soccer match vs Eastbrook</div></div>
    <div class="news-item"><div class="news-date">Fri, April 4:</div><div class="news-text">Varsity Girls' Home Tennis match vs Fernhill</div></div>
    <div class="news-item"><div class="news-date">Wed, April 2:</div><div class="news-text">Varsity Boys' Soccer match vs Calder<br>State Placement Test</div></div>
    <div class="news-item"><div class="news-date">Wed, April 30:</div><div class="news-text">Varsity Boys' Home Soccer match vs Ashford<br>Watch the WKVN broadcast of MVGS presents<br>Hamlet</div></div>
  </section>

  <!-- events -->
  <section class="abs" style="left:187px;top:810px;width:157px;height:180px">
    <h2 class="col-head">Upcoming Events</h2>
    <div class="event" style="top:28px"><div class="event-thumb" role="img" aria-label="Tennis court poster"></div><div class="event-title">4pm Girls' Tennis</div><div class="event-place">Harlow</div><div class="event-btn">More Events</div></div>
    <div class="event" style="top:61px"><div class="event-thumb" role="img" aria-label="Tennis court poster"></div><div class="event-title">4pm Girls' Tennis</div><div class="event-place">Eastbrook</div><div class="event-btn">More Events</div></div>
    <div class="event" style="top:93px"><div class="event-thumb" role="img" aria-label="Tennis match poster"></div><div class="event-title">4:30pm Boys' Tennis</div><div class="event-place">At Pinecrest</div><div class="event-btn">More Events</div></div>
    <div class="event" style="top:126px"><div class="event-thumb" role="img" aria-label="Tennis court poster"></div><div class="event-title">4pm Girls' Tennis</div><div class="event-place">Fernhill</div><div class="event-btn">More Events</div></div>
    <div class="abs" style="left:0;top:159px;width:157px;height:1px;background:#999"></div>
    <div class="abs pager" style="left:0;top:166px"><svg width="6" height="11" viewBox="0 0 6 11"><polyline points="5,1 1,5.5 5,10" fill="none" stroke="#1d6b12" stroke-width="1.4"/></svg>1 / 10<svg width="6" height="11" viewBox="0 0 6 11"><polyline points="1,1 5,5.5 1,10" fill="none" stroke="#1d6b12" stroke-width="1.4"/></svg></div>
  </section>

  <!-- programmes -->
  <h2 class="abs col-head" style="left:358px;top:810px;width:157px">Programmes of Study</h2>
  <div class="abs study-photo" role="img" aria-label="Students working together in a classroom"></div>
  <div class="abs study-list" style="left:366px;top:904px"><h4>Focus Areas</h4><ul><li>Dance</li><li>Literary Arts</li><li>Music</li><li>Technology</li><li>Theatre Arts</li><li>Visual Arts</li></ul></div>
  <div class="abs study-list" style="left:449px;top:904px"><h4>Study Progtams</h4><ul><li>English</li><li>Health and PE</li><li>Math</li><li>Science</li><li>Social Sciences</li><li>World Languages</li></ul></div>

  <!-- footer -->
  <footer class="abs footer">
    <div class="abs footer-col" style="left:54px;top:22px"><h3>Quick Links</h3><ul><li>Home</li><li>Admissions</li><li>Staff Directory</li><li>Information Technology</li><li>Library</li><li>Gradeport (Teachers)</li></ul></div>
    <div class="abs footer-col" style="left:225px;top:22px"><h3>Quick Links</h3><ul><li>MVGS Email</li><li>Online School Payments</li><li>Athletics</li><li>Documents/Forms</li><li>Contact Us</li><li>Gradeport (Parents/Students)</li></ul></div>
    <div class="abs footer-col" style="left:398px;top:22px"><h3>Follow us on</h3><ul class="social"><li><span class="dot" style="background:#3b5998"></span>Friendbook</li><li><span class="dot" style="background:#2aa9e0"></span>Chirper</li><li><span class="dot" style="background:#d34836"></span>Circles +</li></ul></div>
  </footer>
  <div class="abs copyright">Copyright © 2014 Marlowe Valley Regional Governor's School</div>
</main>
</body>
</html>
```